Lumora Goods Energy

Design a 330ml Energy drink pack. Brand Name is 9/4 (meaning Energy lasting 24hrs a day and 7 days a week). The background colour should be silver and a touch of red, very similar but premium to to Vanta Lynx attached. The logo should be a red or black elephant (see samples attached)
The pay-off should be "Feel Good" and "Long Lasting Energy",
at the bottom of the can like zest owl, written in red. Let the font be Cambria or a better option. Can should have complete ingredient listing, space for bar code, manufacturer and brand owners

Target Market(s)

Mainstream Market

Industry/Entity Type

Manufacturer

Requirements
Must have
• Must have strong presence on the shelve

```html
<!DOCTYPE html>
<html lang="en">
<head>
<meta charset="utf-8">
<title>482 Energy Drink – Can Label</title>
<link href="https://fonts.googleapis.com/css2?family=Arimo:wght@400;700&family=Tinos&display=swap" rel="stylesheet">
<style>
  :root {
    --page-top: #f2f4f6;
    --page-bottom: #dfe3e6;
    --can-red: #d9533b;
    --can-red-light: #ec8a73;
    --silver-light: #fbfbfb;
    --silver-mid: #e6e6e6;
    --silver-dark: #cacaca;
    --stripe-grey: #a9a9a9;
    --ink-dark: #2c2c2c;
    --ink-grey: #6a6a6a;
    --band-black: #2a2a2a;
    --white: #ffffff;
  }
  html, body {
    margin: 0;
    padding: 0;
    overflow: hidden;
  }
  .canvas {
    width: 1200px;
    height: 990px;
    position: relative;
    overflow: hidden;
    background: radial-gradient(ellipse at center, var(--page-top) 0%, var(--page-bottom) 100%);
  }
  .can-label {
    position: absolute;
    left: 458px;
    top: 81px;
    width: 286px;
    height: 734px;
    border-radius: 10px 10px 6px 6px;
    overflow: hidden;
    background: linear-gradient(90deg, var(--silver-dark) 0%, var(--silver-light) 45%, var(--silver-mid) 100%);
    box-shadow: 0 10px 30px rgba(0, 0, 0, 0.08);
  }
  .promo-band {
    position: absolute;
    left: 0; right: 0; top: 0;
    height: 178px;
    background: linear-gradient(90deg, var(--can-red) 0%, var(--can-red-light) 45%, var(--can-red) 100%);
    color: var(--white);
    font-family: "Arimo", Arial, sans-serif;
    font-weight: 700;
    text-align: center;
    line-height: 1;
  }
  .promo-percent {
    position: absolute;
    left: 0; right: 0; top: 58px;
    font-size: 60px;
    letter-spacing: 1px;
  }
  .promo-word {
    position: absolute;
    left: 0; right: 0; top: 121px;
    font-size: 60px;
    letter-spacing: 5px;
  }
  .grey-stripe {
    position: absolute;
    left: 0; right: 0; top: 178px;
    height: 18px;
    background: linear-gradient(90deg, var(--stripe-grey), var(--silver-dark), var(--stripe-grey));
  }
  .brand-name {
    position: absolute;
    left: 0; right: 0; top: 218px;
    text-align: center;
    font-family: "Arimo", Arial, sans-serif;
    font-weight: 700;
    font-size: 112px;
    line-height: 1;
    color: var(--ink-grey);
    letter-spacing: 2px;
  }
  .mascot-area {
    position: absolute;
    left: 14px; top: 333px;
    width: 212px;
    height: 256px;
    border-radius: 10px;
    background: radial-gradient(ellipse at center, #9a9a9a 0%, #bdbdbd 70%, rgba(200,200,200,0) 100%);
  }
  .product-type {
    position: absolute;
    left: 0; right: 0; top: 608px;
    text-align: center;
    font-family: "Arimo", Arial, sans-serif;
    font-size: 27px;
    line-height: 1;
    color: var(--ink-dark);
  }
  .payoff-band {
    position: absolute;
    left: 0; right: 0; top: 648px;
    height: 70px;
    display: flex;
    font-family: "Tinos", "Times New Roman", serif;
    font-size: 20px;
    color: var(--white);
  }
  .payoff-left {
    width: 104px;
    background: var(--band-black);
    display: flex;
    align-items: center;
    justify-content: center;
  }
  .payoff-right {
    flex: 1;
    background: var(--can-red);
    display: flex;
    align-items: center;
    justify-content: center;
  }
</style>
</head>
<body>
  <main class="canvas">
    <section class="can-label">
      <header class="promo-band">
        <span class="promo-percent">33%</span>
        <span class="promo-word">MORE</span>
      </header>
      <div class="grey-stripe"></div>
      <div class="brand-name">482</div>
      <div class="mascot-area" role="img" aria-label="Grey elephant mascot illustration with raised trunk"></div>
      <div class="product-type">ENERGY DRINK</div>
      <footer class="payoff-band">
        <div class="payoff-left">Feel good</div>
        <div class="payoff-right">Long lasting energy</div>
      </footer>
    </section>
  </main>
</body>
</html>
```